Medical software helping patients with dry eye disease needs a business card

We have a logo we just need a design for a business card for a Canadian company called LUMA: Dry Eye. We use AI technology to assist optometrists in properly diagnosing patients with dry eye disease reducing wait times in doctors offices and accuracy of diagnosis as well as identifying key possible indicators and tailored treatment plans. The final design should be clean and medical looking. Our mission is to help patients and our logo using blues and whites.

```html
<!DOCTYPE html>
<html lang="en">
<head>
<meta charset="utf-8">
<title>LUMA: Dry Eye — Business Card</title>
<link href="https://fonts.googleapis.com/css2?family=Montserrat:wght@400;500;700&display=swap" rel="stylesheet">
<style>
  :root {
    --bg: #2b2b2d;
    --card: #1e1e1f;
    --blue: #29a8e0;
    --white: #ffffff;
    --text-soft: #e6e6e6;
    --pattern-a: #262627;
    --pattern-b: #3a3a3c;
  }
  * { box-sizing: border-box; margin: 0; padding: 0; }
  html, body { width: 1200px; height: 900px; overflow: hidden; }
  body {
    background: var(--bg);
    font-family: "Montserrat", sans-serif;
    position: relative;
  }
  .card {
    position: absolute;
    left: 285px;
    width: 630px;
    height: 360px;
    border-radius: 16px;
    background: var(--card);
    overflow: hidden;
    box-shadow: 0 18px 40px rgba(0,0,0,.45);
  }
  .card--front { top: 60px; }
  .card--back { top: 480px; }

  .front__band {
    position: absolute; left: 0; right: 0; bottom: 0;
    height: 12px; background: var(--blue);
  }
  .brand {
    position: absolute;
    display: flex; align-items: center; gap: 12px;
  }
  .brand__dot {
    width: 26px; height: 26px; border-radius: 50%;
    background: var(--blue);
    flex: none;
  }
  .brand__name {
    color: var(--white);
    font-weight: 500;
    font-size: 24px;
    white-space: nowrap;
  }
  .card--front .brand { left: 50px; top: 156px; }

  .front__divider {
    position: absolute;
    left: 330px; top: 70px;
    width: 1px; height: 210px;
    background: var(--blue);
  }
  .contact {
    position: absolute;
    left: 360px; top: 82px;
    color: var(--text-soft);
    font-size: 14px;
    line-height: 1.45;
  }
  .contact__name {
    color: var(--blue);
    font-weight: 700;
    font-size: 21px;
    text-transform: uppercase;
    letter-spacing: .5px;
  }
  .contact__role { font-size: 15px; margin-bottom: 14px; }
  .contact__address { margin-bottom: 14px; }
  .contact__list { list-style: none; }
  .contact__item { display: flex; align-items: center; gap: 9px; }
  .contact__icon { width: 13px; height: 13px; flex: none; }

  .back__pattern {
    position: absolute; inset: 0;
    background: linear-gradient(135deg, var(--pattern-a) 0%, var(--pattern-b) 55%, var(--pattern-a) 100%);
  }
  .card--back .brand { left: 44px; bottom: 44px; }
</style>
</head>
<body>

<section class="card card--front" aria-label="Business card front">
  <div class="brand">
    <span class="brand__dot"></span>
    <span class="brand__name">LUMA: Dry Eye</span>
  </div>
  <div class="front__divider"></div>
  <div class="contact">
    <p class="contact__name">Daniel Rourke</p>
    <p class="contact__role">CEO/Founder</p>
    <p class="contact__address">P.O. Box 3870 Harbour Road<br>Halifax NS B3H 2Y1</p>
    <ul class="contact__list">
      <li class="contact__item">
        <svg class="contact__icon" viewBox="0 0 24 24" aria-hidden="true"><path fill="var(--blue)" d="M6.6 10.8a15 15 0 0 0 6.6 6.6l2.2-2.2c.3-.3.7-.4 1-.2 1.1.4 2.3.6 3.6.6.6 0 1 .4 1 1V20c0 .6-.4 1-1 1A17 17 0 0 1 3 4c0-.6.4-1 1-1h3.5c.6 0 1 .4 1 1 0 1.3.2 2.5.6 3.6.1.3 0 .7-.2 1z"/></svg>
        <span>(555) 014 2290</span>
      </li>
      <li class="contact__item">
        <svg class="contact__icon" viewBox="0 0 24 24" aria-hidden="true"><path fill="var(--blue)" d="M2 5h20v14H2z"/><path fill="none" stroke="var(--card)" stroke-width="2" d="M2 5l10 8 10-8"/></svg>
        <span>info@lumadryeye.com</span>
      </li>
      <li class="contact__item">
        <svg class="contact__icon" viewBox="0 0 24 24" aria-hidden="true"><g fill="none" stroke="var(--blue)" stroke-width="2"><circle cx="12" cy="12" r="10"/><ellipse cx="12" cy="12" rx="4.5" ry="10"/><path d="M2 12h20M4 7h16M4 17h16"/></g></svg>
        <span>www.lumadryeye.com</span>
      </li>
    </ul>
  </div>
  <div class="front__band"></div>
</section>

<section class="card card--back" aria-label="Business card back">
  <div class="back__pattern" role="img" aria-label="Repeating tone-on-tone decorative pattern in dark greys"></div>
  <div class="brand">
    <span class="brand__dot"></span>
    <span class="brand__name">LUMA: Dry Eye</span>
  </div>
</section>

</body>
</html>
```